Lantern Airfields Homepage Design Update

here's the current site - http://lanternairfields.example/

client is not happy with overall look.

keeping the same info - intro text, headlines, featured media excepts and general navigation options - can you come up with a nicer, slicker look for this homepage?

UPDATE: since it was asked by designer.. the general layout doesnt have to be the same. its not required to have a big image, with text below that and then smaller images/text below that. as long as we have the same content on the page, it can organized and designed in any way,

client like big images, so one way or the other, keep that... but feel free to reorganize content, explore different ways of framing it, and/or anything else. make this homepage pop!

for the designer that wins this, we'll start an additional project to update the interior.

let me know if any questions..

thanks!

marcus

Target Market(s)

aviation industry professionals, local governments, general public

Number of Pages Required

1 page

Font styles to use
Sans Serif

Requirements
Must have
• big image somewhere. same content as on current site, just designed differently.

```html
<!DOCTYPE html>
<html lang="en">
<head>
<meta charset="utf-8">
<title>Lantern Airfields — Home</title>
<link rel="stylesheet" href="https://fonts.googleapis.com/css2?family=Open+Sans:wght@400;600&family=Roboto+Condensed:wght@700&display=swap">
<style>
  :root {
    --navy: #12123f;
    --ink: #15164a;
    --white: #ffffff;
    --line: #c9c9d3;
    --sky-top: #4f86b9;
    --sky-mid: #a9c3d4;
    --sky-glow: #f1e2b8;
    --photo-blue: #2a4f9a;
    --photo-dark: #3b3e52;
  }
  * { box-sizing: border-box; margin: 0; padding: 0; }
  html, body { width: 1200px; height: 1000px; overflow: hidden; background: var(--white); }
  body { position: relative; font-family: "Open Sans", Arial, sans-serif; color: var(--ink); }

  .page {
    position: absolute; left: 188px; top: 25px; width: 822px; height: 952px;
    background: var(--white); box-shadow: 0 0 4px rgba(0,0,0,.35);
  }
  .site-header { position: absolute; left: 0; top: 0; width: 100%; height: 60px; }
  .brand {
    position: absolute; left: 70px; top: 22px; display: flex; align-items: center; gap: 8px;
    font-size: 15px; color: var(--ink); letter-spacing: .5px;
  }
  .brand-dot { width: 12px; height: 12px; border-radius: 50%; background: var(--ink); }
  .social { position: absolute; right: 88px; top: 13px; display: flex; gap: 11px; }
  .social-button {
    width: 33px; height: 33px; border-radius: 50%; border: 1px solid var(--line); position: relative;
  }
  .social-button::after {
    content: ""; position: absolute; left: 10px; top: 10px; width: 11px; height: 11px;
    border-radius: 2px; background: var(--navy);
  }

  .hero {
    position: absolute; left: 0; top: 60px; width: 100%; height: 433px;
    background: linear-gradient(180deg, var(--sky-top) 0%, var(--sky-mid) 40%, var(--sky-glow) 85%, #e9dcc0 100%);
  }
  .main-nav {
    position: absolute; left: 200px; top: 60px; width: 622px; height: 35px;
    background: var(--navy); border-bottom-left-radius: 40px 35px;
    display: flex; align-items: center; padding-left: 46px; gap: 0;
  }
  .main-nav a { color: var(--white); text-decoration: none; font-size: 15.5px; }
  .main-nav a + a { margin-left: 30px; }
  .main-nav a.nav-contact { margin-left: 36px; }

  .tagline {
    position: absolute; left: 0; top: 560px; width: 100%; text-align: center;
    font-family: "Roboto Condensed", "Arial Narrow", sans-serif; font-weight: 700;
    font-size: 27px; line-height: 33px; color: var(--ink);
  }
  .read-more {
    position: absolute; left: 370px; top: 636px; width: 80px; height: 25px;
    border: 1px solid var(--ink); border-radius: 13px; font-size: 11px; color: var(--ink);
    display: flex; align-items: center; justify-content: center; gap: 3px; text-decoration: none;
  }

  .featured {
    position: absolute; left: 34px; top: 744px; width: 758px; height: 133px;
    border: 1px solid var(--line); border-radius: 20px;
  }
  .featured-title {
    position: absolute; left: 0; top: 8px; width: 100%; text-align: center;
    font-size: 15px; font-weight: 600; color: var(--ink);
  }
  .carousel-arrow { position: absolute; top: 64px; }
  .carousel-arrow.prev { left: 16px; }
  .carousel-arrow.next { left: 686px; }
  .media-item { position: absolute; top: 40px; display: flex; align-items: center; }
  .media-item.first { left: 102px; }
  .media-item.second { left: 362px; }
  .media-thumb { width: 81px; height: 81px; }
  .thumb-capitol { background: linear-gradient(180deg, var(--photo-blue) 0%, #6d86c2 60%, #c9a9b8 100%); }
  .thumb-portrait { background: linear-gradient(180deg, var(--photo-blue) 0%, #4456a0 50%, var(--photo-dark) 100%); }
  .media-caption { font-size: 10.5px; line-height: 13px; text-align: center; color: var(--ink); }
  .media-item.first .media-caption { width: 172px; }
  .media-item.second .media-caption { width: 212px; margin-left: 2px; }

  .site-footer {
    position: absolute; left: 0; top: 910px; width: 100%; height: 42px; background: var(--navy);
    display: flex; align-items: center; padding-left: 159px; font-size: 10px; color: var(--white);
  }
  .footer-links { display: flex; margin-left: 16px; }
  .footer-links a { color: var(--white); text-decoration: none; padding: 0 4px; line-height: 14px; }
  .footer-links a + a { border-left: 1px solid var(--white); }
</style>
</head>
<body>
  <div class="page">
    <header class="site-header">
      <div class="brand"><span class="brand-dot"></span><span>Lantern Airfields</span></div>
      <div class="social">
        <span class="social-button" aria-label="Social profile"></span>
        <span class="social-button" aria-label="Professional profile"></span>
      </div>
    </header>

    <div class="hero" role="img" aria-label="Passenger jet taking off into a bright sky with clouds at sunset"></div>

    <nav class="main-nav">
      <a href="#">About</a>
      <a href="#">Services</a>
      <a href="#">Airports</a>
      <a href="#">News &amp; Media</a>
      <a href="#" class="nav-contact">Contact</a>
      <a href="#" class="nav-contact">Employees</a>
    </nav>

    <h1 class="tagline">Bringing private, free enterprise business practices<br>To airports throughout the U.S.</h1>
    <a href="#" class="read-more">Read More
      <svg width="6" height="9" viewBox="0 0 6 9"><polyline points="1,1 5,4.5 1,8" fill="none" stroke="currentColor" stroke-width="1.6"/></svg>
    </a>

    <section class="featured">
      <h2 class="featured-title">FEATURED MEDIA</h2>
      <svg class="carousel-arrow prev" width="52" height="18" viewBox="0 0 52 18">
        <polyline points="10,2 3,9 10,16" fill="none" stroke="#d4d4dd" stroke-width="4"/>
        <polyline points="20,2 13,9 20,16" fill="none" stroke="#a5a6bb" stroke-width="4"/>
        <polyline points="30,2 23,9 30,16" fill="none" stroke="#6e7093" stroke-width="4"/>
        <polyline points="40,2 33,9 40,16" fill="none" stroke="#12123f" stroke-width="4"/>
      </svg>
      <div class="media-item first">
        <div class="media-thumb thumb-capitol" role="img" aria-label="Capitol dome against a blue sky"></div>
        <p class="media-caption">Lantern Participates in Airport P3<br>Congressional Roundtable</p>
      </div>
      <div class="media-item second">
        <div class="media-thumb thumb-portrait" role="img" aria-label="Portrait of the new chairman"></div>
        <p class="media-caption">Lantern Airfields Apoints<br>Daniel K. Whitcombe as Chairman of the Board</p>
      </div>
      <svg class="carousel-arrow next" width="52" height="18" viewBox="0 0 52 18">
        <polyline points="12,2 19,9 12,16" fill="none" stroke="#12123f" stroke-width="4"/>
        <polyline points="22,2 29,9 22,16" fill="none" stroke="#6e7093" stroke-width="4"/>
        <polyline points="32,2 39,9 32,16" fill="none" stroke="#a5a6bb" stroke-width="4"/>
        <polyline points="42,2 49,9 42,16" fill="none" stroke="#d4d4dd" stroke-width="4"/>
      </svg>
    </section>

    <footer class="site-footer">
      <span>Copyright 2015 Lantern.</span>
      <nav class="footer-links">
        <a href="#">Home</a><a href="#">About</a><a href="#">Services</a><a href="#">Airports</a>
        <a href="#">News &amp; Media</a><a href="#">Contact</a><a href="#">Employees</a><a href="#">Terms Of Use</a>
      </nav>
    </footer>
  </div>
</body>
</html>
```